Business card design for strategy and management consulting company. Would like to have a clean and professional business card, based on the attached logo. The company is a strategy and management consulting company focusing on sustainable business modlels based on economic, social and environmental market opportunities. Preferably the logo should be included on both sides of the design.

Industry/Entity Type

Business

Contact Information for Business Card

Håvard Lilleby, CEO/Management consultant
havard.lilleby@quarvenpartners.example
Mob: +47 948 26 317
Office: Vikfjell gate 14, pb 312 sentrum, N-0172 Oslo Norway

Requirements
Must have
• Include attached logo
Nice to have
• Would like to have the logo on both sides
Should not have
• Many colours.

```html
<!DOCTYPE html>
<html lang="en">
<head>
<meta charset="utf-8">
<title>Quarven business card</title>
<link href="https://fonts.googleapis.com/css2?family=Open+Sans:wght@400;600;700&display=swap" rel="stylesheet">
<style>
  :root {
    --ink: #1f1d1c;
    --yellow: #f6d80f;
    --paper: #ffffff;
    --backdrop: #e9e9e7;
    --muted: #555;
  }
  * { margin: 0; padding: 0; box-sizing: border-box; }
  html, body { width: 1200px; height: 900px; overflow: hidden; }
  body {
    background: var(--backdrop);
    font-family: "Open Sans", Arial, sans-serif;
    color: var(--ink);
    display: flex;
    flex-direction: column;
    align-items: center;
    justify-content: center;
    gap: 40px;
  }
  .card {
    position: relative;
    width: 600px;
    height: 343px;
    overflow: hidden;
    box-shadow: 0 6px 18px rgba(0,0,0,0.18);
  }
  .wordmark {
    display: flex;
    align-items: center;
    gap: 8px;
    font-weight: 700;
    color: var(--ink);
    letter-spacing: -1px;
    line-height: 1;
  }
  .wordmark-dot {
    width: 10px;
    height: 10px;
    background: var(--yellow);
    align-self: flex-start;
    margin-top: 4px;
  }

  /* Front */
  .card-front { background: var(--yellow); }
  .front-dark {
    position: absolute;
    left: 0; top: 0; bottom: 0;
    width: 44%;
    background: var(--ink);
  }
  .front-panel {
    position: absolute;
    left: 26%;
    top: 29%;
    width: 47%;
    height: 44%;
    background: var(--paper);
    display: flex;
    align-items: center;
    justify-content: center;
  }
  .front-panel .wordmark { font-size: 50px; }

  /* Back */
  .card-back { background: var(--paper); }
  .back-logo {
    position: absolute;
    left: 70px;
    bottom: 70px;
  }
  .back-logo .wordmark { font-size: 56px; }
  .contact {
    position: absolute;
    left: 318px;
    top: 52px;
  }
  .contact-name { font-size: 21px; font-weight: 600; line-height: 1.1; }
  .contact-role { font-size: 9px; color: var(--muted); margin: 2px 0 12px 2px; }
  .contact-list { list-style: none; }
  .contact-item {
    display: flex;
    align-items: flex-start;
    gap: 8px;
    font-size: 12.5px;
    line-height: 1.35;
    margin-bottom: 4px;
  }
  .contact-icon { flex: 0 0 16px; width: 16px; height: 16px; margin-top: 1px; }
</style>
</head>
<body>

  <section class="card card-front" aria-label="Card front">
    <div class="front-dark"></div>
    <div class="front-panel">
      <div class="wordmark"><span>Quarven</span><span class="wordmark-dot"></span></div>
    </div>
  </section>

  <section class="card card-back" aria-label="Card back">
    <div class="contact">
      <p class="contact-name">Håvard Lilleby</p>
      <p class="contact-role">CEO/Management consultant</p>
      <ul class="contact-list">
        <li class="contact-item">
          <svg class="contact-icon" viewBox="0 0 16 16" aria-hidden="true">
            <rect width="16" height="16" fill="var(--ink)"/>
            <rect x="5" y="2.5" width="6" height="11" rx="1" fill="none" stroke="var(--yellow)" stroke-width="1.4"/>
            <rect x="7" y="11" width="2" height="1" fill="var(--yellow)"/>
          </svg>
          <span>+47 948 26 317</span>
        </li>
        <li class="contact-item">
          <svg class="contact-icon" viewBox="0 0 16 16" aria-hidden="true">
            <rect width="16" height="16" fill="var(--ink)"/>
            <rect x="2.5" y="4.5" width="11" height="7" fill="var(--yellow)"/>
            <path d="M2.5 4.5 L8 8.8 L13.5 4.5" fill="none" stroke="var(--ink)" stroke-width="1"/>
          </svg>
          <span>havard.lilleby@quarvenpartners.example</span>
        </li>
        <li class="contact-item">
          <svg class="contact-icon" viewBox="0 0 16 16" aria-hidden="true">
            <rect width="16" height="16" fill="var(--ink)"/>
            <path d="M8 2.5 C5.5 2.5 4 4.2 4 6.3 C4 9 8 13.5 8 13.5 C8 13.5 12 9 12 6.3 C12 4.2 10.5 2.5 8 2.5 Z" fill="var(--yellow)"/>
            <circle cx="8" cy="6.3" r="1.5" fill="var(--ink)"/>
          </svg>
          <span>Vikfjell gate 14,<br>pb 312 sentrum, N-0172 Oslo Norway</span>
        </li>
      </ul>
    </div>
    <div class="back-logo">
      <div class="wordmark"><span>Quarven</span><span class="wordmark-dot"></span></div>
    </div>
  </section>

</body>
</html>
```